Creative design for KWP Businesscard!

We would like a creative business card for our company The Copper Mill. We situated in Barcelona and setup software development teams for companies in Belgium, Holland.

Orange is related to Holland.
KWP means cool in Dutch

* An Overview / Background of the Business & Services
o Setup and manage developer teams in Barcelona for for companies
in Holland, Belgium.
* The Target Market / Audience you are trying to reach
o Companies in Holland searching for developers
* Design Specifics; any preferences or ideas for Style, Colour,
Imagery, etc
o Orange, professional, fancy
o The Copper Mill (KWP) means cool , good, nice

Target Market(s)

Companies in Holland searching for developers

Industry/Entity Type

Business

Contact Information for Business Card

Company name: The Copper Mill

Name: Maarten Oostveld

Title: Managing director (not necessary)

Email: maarten@thecoppermill.es

web: www.thecoppermill.es

Phone: (+34) 932 478 013

Mobile: (+34) 662 307 594

Font styles to use
Other font styles liked:
• Bookman Old Style or Rockwell

Requirements
Must have
• Setup and manage developer teams in Barcelona for for companies
• in Holland, Belgium.

```html
<!DOCTYPE html>
<html lang="en">
<head>
<meta charset="utf-8">
<title>The Copper Mill – Business Card</title>
<link rel="stylesheet" href="https://fonts.googleapis.com/css2?family=Open+Sans:wght@400;600;700&display=swap">
<style>
  :root {
    --orange: #d9703a;
    --charcoal: #3c3c3b;
    --ink: #2f2f2f;
    --paper: #ffffff;
    --backdrop: #e6e6e6;
  }
  * { box-sizing: border-box; margin: 0; padding: 0; }
  html, body { width: 1200px; height: 800px; overflow: hidden; }
  body {
    background: var(--backdrop);
    font-family: "Open Sans", Arial, sans-serif;
    display: flex;
    align-items: center;
    justify-content: center;
    gap: 40px;
  }
  .card {
    position: relative;
    width: 540px;
    height: 310px;
    background: var(--paper);
    box-shadow: 0 2px 10px rgba(0,0,0,0.12);
    overflow: hidden;
  }
  /* Front */
  .brand {
    position: absolute;
    left: 0;
    top: 0;
    width: 268px;
    height: 262px;
    display: flex;
    align-items: center;
    justify-content: center;
  }
  .brand-name {
    font-family: "Open Sans", Arial, sans-serif;
    font-weight: 700;
    font-size: 56px;
    line-height: 1;
    color: var(--charcoal);
    letter-spacing: 2px;
  }
  .divider {
    position: absolute;
    left: 268px;
    top: 36px;
    width: 2px;
    height: 190px;
    background: var(--charcoal);
  }
  .contact {
    position: absolute;
    left: 290px;
    top: 44px;
    right: 14px;
  }
  .person-name {
    font-weight: 600;
    font-size: 21px;
    color: var(--charcoal);
    line-height: 1.15;
  }
  .person-title {
    font-size: 15px;
    color: var(--orange);
    letter-spacing: 0.3px;
  }
  .company {
    margin-top: 22px;
    font-weight: 700;
    font-size: 15px;
    color: var(--orange);
  }
  .details { list-style: none; margin-top: 2px; }
  .details li {
    display: flex;
    align-items: center;
    gap: 10px;
    font-size: 13px;
    line-height: 21px;
    color: var(--ink);
  }
  .details svg { width: 10px; height: 10px; flex: none; fill: var(--orange); }
  .bands {
    position: absolute;
    left: 0;
    bottom: 8px;
    width: 540px;
    height: 30px;
  }
  /* Back */
  .card-back {
    display: flex;
    flex-direction: column;
    align-items: center;
    justify-content: center;
    gap: 18px;
    text-align: center;
  }
  .card-back .brand-name { font-size: 52px; }
  .tagline {
    max-width: 360px;
    font-size: 13px;
    line-height: 1.5;
    color: var(--charcoal);
  }
</style>
</head>
<body>
  <section class="card card-front">
    <div class="brand">
      <span class="brand-name">KWP</span>
    </div>
    <div class="divider"></div>
    <div class="contact">
      <p class="person-name">Maarten Oostveld</p>
      <p class="person-title">Managing director</p>
      <p class="company">The Copper Mill</p>
      <ul class="details">
        <li><svg viewBox="0 0 10 10" aria-hidden="true"><path d="M0 2h10v6H0z M0 2l5 3.5L10 2" stroke="#fff" stroke-width="0.8"/></svg>maarten@thecoppermill.es</li>
        <li><svg viewBox="0 0 10 10" aria-hidden="true"><path d="M1 3c0-1.5 8-1.5 8 0v1H7V3H3v1H1z M2 5h6l1 4H1z"/></svg>(+34) 932 478 013</li>
        <li><svg viewBox="0 0 10 10" aria-hidden="true"><path d="M2.5 0h5v10h-5z M3.3 1v7h3.4V1z"/></svg>(+34) 662 307 594</li>
        <li><svg viewBox="0 0 10 10" aria-hidden="true"><circle cx="5" cy="5" r="5"/><path d="M0 5h10M5 0v10" stroke="#fff" stroke-width="0.7"/></svg>www.thecoppermill.es</li>
      </ul>
    </div>
    <svg class="bands" viewBox="0 0 540 30" aria-hidden="true">
      <polygon points="0,0 390,0 418,30 0,30" fill="var(--orange)"/>
      <polygon points="425,0 540,0 540,30 450,30" fill="var(--charcoal)"/>
    </svg>
  </section>

  <section class="card card-back">
    <span class="brand-name">KWP</span>
    <p class="tagline">Setup and manage developer teams in Barcelona for companies in Holland, Belgium.</p>
  </section>
</body>
</html>
```